DL Flyer for garden consultants. I will supply text and logo

To design an eye catching but simple, uncluttered flyer for letter box distribution. The text and logo are provided.

```html
<!DOCTYPE html>
<html lang="en">
<head>
<meta charset="utf-8">
<title>Fernlea Garden Consultants – DL Flyer</title>
<link href="https://fonts.googleapis.com/css2?family=Didact+Gothic&family=Pinyon+Script&family=Arimo:wght@400;700&display=swap" rel="stylesheet">
<style>
  :root {
    --lime-light: #d4e12a;
    --lime: #b9d72f;
    --lime-deep: #8fc63c;
    --brand-green: #86c440;
    --white: #ffffff;
    --ink: #1a1a1a;
    --list-green: #0f7a3c;
    --list-sub: #17a047;
    --sky-top: #1b7fd6;
    --sky-mid: #6fc0f0;
    --sky-glow: #e9f7fb;
    --hill: #8ed13a;
  }
  * { box-sizing: border-box; margin: 0; padding: 0; }
  html, body { width: 1130px; height: 1200px; overflow: hidden; }
  body {
    position: relative;
    background: linear-gradient(135deg, var(--lime-light) 0%, var(--lime) 50%, var(--lime-deep) 100%);
    font-family: "Didact Gothic", "Century Gothic", sans-serif;
  }
  .fold {
    position: absolute; top: 0; left: 560px; width: 6px; height: 1200px;
    background: rgba(255,255,255,0.18);
  }
  .logo-box {
    position: absolute; background: var(--white);
    display: flex; align-items: center; justify-content: center; gap: 18px;
  }
  .logo-box--left { left: 59px; top: 33px; width: 461px; height: 204px; }
  .logo-box--right { left: 621px; top: 35px; width: 462px; height: 203px; }
  .brand-mark { width: 62px; height: 62px; border-radius: 50%; background: var(--brand-green); flex: none; }
  .brand-name { color: var(--brand-green); font-family: "Didact Gothic", sans-serif; font-weight: 400; line-height: 1; }
  .brand-name .main { display: block; font-size: 64px; }
  .brand-name .sub { display: block; font-size: 15px; letter-spacing: 3px; margin-top: 8px; text-transform: uppercase; }

  .panel { position: absolute; overflow: hidden; background: var(--white); }
  .panel--left { left: 59px; top: 250px; width: 461px; height: 905px; }
  .panel--right { left: 626px; top: 258px; width: 457px; height: 897px; }

  .sky {
    position: absolute; left: 0; top: 0; width: 461px; height: 330px;
    background:
      radial-gradient(ellipse 260px 200px at 130px 250px, var(--sky-glow) 0%, rgba(233,247,251,0) 70%),
      linear-gradient(180deg, var(--sky-top) 0%, var(--sky-mid) 55%, var(--hill) 80%, var(--white) 100%);
  }
  .grass-field { position: absolute; left: 0; width: 100%; }
  .grass-field--left { bottom: 0; height: 195px; }
  .grass-field--right { top: 0; height: 740px; }

  .question {
    position: absolute; left: 86px; top: 140px;
    font-size: 55px; line-height: 70px; color: var(--ink);
  }
  .question .initial { font-family: "Pinyon Script", cursive; font-size: 68px; }
  .well {
    position: absolute; left: 162px; top: 580px;
    font-family: "Pinyon Script", cursive; font-size: 100px; color: var(--ink);
  }
  .cta { position: absolute; width: 100%; text-align: center; font-family: "Arimo", Arial, sans-serif; font-weight: 700; }
  .cta .lead { font-size: 17px; }
  .cta .url { font-size: 21px; margin-top: 4px; }
  .cta--left { bottom: 32px; color: var(--white); }
  .cta--right { bottom: 30px; color: var(--ink); text-align: right; padding-right: 28px; }

  .help {
    position: absolute; left: 20px; top: 90px; color: var(--white);
    font-family: "Pinyon Script", cursive; font-size: 70px; line-height: 1; white-space: nowrap;
  }
  .help .dots { font-family: "Arimo", sans-serif; font-weight: 700; font-size: 24px; }
  .services {
    position: absolute; left: 18px; top: 194px; width: 427px; height: 349px;
    background: var(--white); border-radius: 22px; padding: 32px 18px 0 22px;
    list-style: none; font-family: "Arimo", Arial, sans-serif;
  }
  .services li { position: relative; padding-left: 26px; margin-bottom: 24px; }
  .services li::before { content: "•"; position: absolute; left: 0; top: -2px; color: var(--list-green); font-size: 22px; }
  .services .title { display: block; color: var(--list-green); font-weight: 700; font-size: 20px; line-height: 26px; }
  .services .note { display: block; color: var(--list-sub); font-size: 19px; line-height: 26px; }
  .services .note.indent { padding-left: 40px; }
  .mini-logo {
    position: absolute; right: 28px; top: 745px; display: flex; align-items: center; gap: 8px;
    color: var(--brand-green);
  }
  .mini-logo .brand-mark { width: 24px; height: 24px; }
  .mini-logo .brand-name .main { font-size: 26px; }
  .mini-logo .brand-name .sub { font-size: 8px; letter-spacing: 1px; margin-top: 3px; }
</style>
</head>
<body>
  <div class="fold"></div>

  <header class="logo-box logo-box--left">
    <span class="brand-mark"></span>
    <span class="brand-name"><span class="main">Fernlea</span><span class="sub">Garden Consultants</span></span>
  </header>

  <section class="panel panel--left">
    <div class="sky" role="img" aria-label="Sunny blue sky over a green grassy hill with clover and butterflies"></div>
    <svg class="grass-field grass-field--left" viewBox="0 0 461 195" preserveAspectRatio="none" role="img" aria-label="Lush green lawn with small butterflies">
      <defs>
        <linearGradient id="lawnFront" x1="0" y1="0" x2="0" y2="1">
          <stop offset="0" stop-color="#6fc52c"/>
          <stop offset="1" stop-color="#2f8f1f"/>
        </linearGradient>
      </defs>
      <path d="M0 10 C120 -5 200 45 300 40 C380 36 430 15 461 10 L461 195 L0 195 Z" fill="url(#lawnFront)"/>
    </svg>
    <p class="question"><span class="initial">H</span>ave<br>you been<br>thinking<br>about<br>your garden<br>lately?</p>
    <p class="well">Well.....</p>
    <div class="cta cta--left">
      <div class="lead">Check us out at</div>
      <div class="url">www.fernleagardenconsultants.com.au</div>
    </div>
  </section>

  <header class="logo-box logo-box--right">
    <span class="brand-mark"></span>
    <span class="brand-name"><span class="main">Fernlea</span><span class="sub">Garden Consultants</span></span>
  </header>

  <section class="panel panel--right">
    <svg class="grass-field grass-field--right" viewBox="0 0 457 740" preserveAspectRatio="none" role="img" aria-label="Close-up of lush green lawn with small butterflies">
      <defs>
        <linearGradient id="lawnInside" x1="0" y1="0" x2="0" y2="1">
          <stop offset="0" stop-color="#3f9f22"/>
          <stop offset="0.5" stop-color="#5fbb2a"/>
          <stop offset="1" stop-color="#3a9a21"/>
        </linearGradient>
      </defs>
      <path d="M0 0 L457 0 L457 700 C380 690 320 730 220 735 C120 740 60 700 0 690 Z" fill="url(#lawnInside)"/>
    </svg>
    <p class="help"><span class="dots">......</span> We can help.</p>
    <ul class="services">
      <li><span class="title">Garden Assessment Consultation and Report</span>
        <span class="note">...... information vital to ensuring</span>
        <span class="note indent">your dream becomes reality!</span></li>
      <li><span class="title">Pre Sale Consultation and Report</span>
        <span class="note">.....&nbsp; maximise your sale dollar!</span></li>
      <li><span class="title">Develop a Plant Portfolio</span>
        <span class="note">..... successfully navigate</span>
        <span class="note indent">the plant maze!</span></li>
    </ul>
    <div class="mini-logo">
      <span class="brand-mark"></span>
      <span class="brand-name"><span class="main">Fernlea</span><span class="sub">Garden Consultants</span></span>
    </div>
    <div class="cta cta--right">
      <div class="lead">Check us out at</div>
      <div class="url">www.fernleagardenconsultants.com.au</div>
    </div>
  </section>
</body>
</html>
```